Design a Professional Stationery

Hi everyone,
I would like to make a design of stationery for my company Kestrel Wrap (www.kestrelwrap-example.com).
General Info: We are manufacturers of packaging supplies (poly bubble mailers, kraft bubble mailers, bubble wrap, tape, stretch film). We have couple of big warehouses in Los Angeles and New Jersey that serves East and West Coasts. We store lot of boxes with our product. We are wholesalers so we work with big serious distributors.

Project Goals: Create a business stationery that will look professional, modern and straight to the point. Colors: Dark blue, white, light blue (please see the web site). Blue is the color of success.
I want them to be presentable. As you might need to imagine my team will walk around the businesses and leave folders with information at clients table. We will distribute them at the trade shows, business meetings etc.
Updates

Target Market(s)

Business professionals looking for professional wholesaler manufacturer.

Industry/Entity Type

It Company

Font styles to use
Serif
Sans Serif

Colors
3276b5
0255a3
85acd3
cedeed
eaf1f7

Requirements
Must have
• People photos, product photos, add professional warehouse photos, truck, machinery.
Nice to have
• NLP
Should not have
• Use your imagination, no limits so far

```html
<!DOCTYPE html>
<html lang="en">
<head>
<meta charset="utf-8">
<title>Kestrel Wrap Stationery</title>
<link rel="stylesheet" href="https://fonts.googleapis.com/css2?family=Questrial&display=swap">
<style>
  :root {
    --navy: #0a2d5e;
    --blue: #3276b5;
    --blue-mid: #85acd3;
    --blue-pale: #cedeed;
    --paper: #f2f2f2;
    --ink: #4a4a4a;
    --stage: #cfcfcf;
  }
  * { margin: 0; padding: 0; box-sizing: border-box; }
  html, body { width: 1200px; height: 1000px; overflow: hidden; }
  body { background: var(--stage); font-family: "Questrial", sans-serif; color: var(--ink); position: relative; }

  .piece { position: absolute; overflow: hidden; }
  .paper { background: var(--paper); }
  .navy { background: var(--navy); }

  /* wordmark: invented name in the body font, one colour, one weight, plus one plain circle */
  .wordmark { position: absolute; display: flex; align-items: center; gap: 0.3em; font-family: "Questrial", sans-serif; font-weight: 400; line-height: 1; white-space: nowrap; }
  .wordmark.centered { left: 0; right: 0; justify-content: center; }
  .wordmark-dot { width: 0.42em; height: 0.42em; border-radius: 50%; }
  .wordmark.on-dark { color: #fff; }
  .wordmark.on-dark .wordmark-dot { background: var(--blue-mid); }
  .wordmark.on-light { color: var(--navy); }
  .wordmark.on-light .wordmark-dot { background: var(--blue); }

  /* colour bands */
  .band { position: absolute; display: flex; }
  .band span { flex: 1; }
  .band .c1 { background: var(--blue); }
  .band .c2 { background: var(--blue-mid); }
  .band .c3 { background: var(--blue-pale); }
  .base-rule { position: absolute; left: 0; right: 0; background: var(--navy); }

  /* folder */
  .folder { left: 152px; top: 40px; width: 431px; height: 560px; border-radius: 4px; }
  .folder-spine { position: absolute; left: 18px; top: 0; bottom: 0; width: 4px; border-left: 1px solid #0d3a73; border-right: 1px solid #0d3a73; }

  /* letterhead */
  .letterhead { left: 616px; top: 62px; width: 417px; height: 538px; }
  .contact { position: absolute; font-size: 6.2px; line-height: 7.4px; color: #333; }
  .contact-line { display: flex; align-items: center; gap: 3px; }
  .icon { width: 6px; height: 6px; background: #333; border-radius: 1px; display: inline-block; }
  .letter-body { position: absolute; left: 39px; top: 176px; width: 342px; font-size: 6.1px; line-height: 7.2px; text-align: justify; color: #555; }
  .letter-body p { margin-bottom: 6px; }
  .letter-body .salute { color: #333; margin-bottom: 7px; }
  .signoff { margin-top: 12px; }
  .signoff strong { display: block; color: #333; }
  .signature { position: absolute; left: 88px; top: 348px; width: 90px; height: 42px; background: linear-gradient(90deg, #e7ebf3, #dbe2ef); border-radius: 3px; }

  /* envelopes */
  .envelope-front { left: 117px; top: 630px; width: 465px; height: 202px; }
  .env-address { position: absolute; left: 17px; top: 179px; font-size: 6.2px; color: #444; }
  .envelope-back { left: 616px; top: 629px; width: 466px; height: 202px; }
  .flap { position: absolute; left: 0; top: 0; }

  /* business cards */
  .card-front { left: 410px; top: 860px; width: 173px; height: 100px; }
  .card-back { left: 616px; top: 860px; width: 173px; height: 100px; }
  .card-name { position: absolute; left: 9px; top: 22px; font-size: 7px; color: var(--blue); letter-spacing: 0.04em; }
  .card-role { position: absolute; left: 9px; top: 30px; font-size: 5px; color: #444; }
  .card-contact { position: absolute; left: 9px; top: 69px; font-size: 4.4px; line-height: 5.6px; color: #333; }
  .card-contact .icon { width: 4px; height: 4px; }
  .card-address { position: absolute; right: 10px; top: 70px; font-size: 4.4px; line-height: 5.6px; color: #333; text-align: right; }
</style>
</head>
<body>

<!-- Presentation folder -->
<section class="piece navy folder" aria-label="Presentation folder">
  <div class="folder-spine"></div>
  <div class="wordmark on-dark" style="left:172px; top:104px; font-size:27px;">
    <span>Kestrel Wrap</span><span class="wordmark-dot"></span>
  </div>
  <div class="band" style="left:169px; bottom:0; width:189px; height:8px;">
    <span class="c1"></span><span class="c2"></span><span class="c3"></span>
  </div>
</section>

<!-- Letterhead -->
<section class="piece paper letterhead" aria-label="Letterhead">
  <div class="wordmark on-light" style="left:39px; top:44px; font-size:17px;">
    <span>Kestrel Wrap</span><span class="wordmark-dot"></span>
  </div>
  <div class="contact" style="left:289px; top:40px;">
    <div class="contact-line"><span class="icon"></span>555-014-2290</div>
    <div class="contact-line"><span class="icon"></span>info@kestrelwrap-example.com</div>
    <div class="contact-line"><span class="icon"></span>www.kestrelwrap-example.com</div>
    <div style="margin-top:2px;">4200 Harbor Row</div>
    <div>Valley Park CA 90000</div>
  </div>
  <div class="letter-body">
    <p class="salute">Dear sir,</p>
    <p>Thank you for your continued interest in our packaging range. We manufacture and supply poly bubble mailers, kraft bubble mailers, bubble wrap, packing tape and stretch film to distributors across both coasts. Our warehouses in the west and the east hold deep stock at all times, so every order can leave our docks quickly and reach your customers in good condition, on time and without surprises.</p>
    <p>This folder gathers our current price sheets, product specifications and shipping terms in one place. Please review the enclosed pages and share them with your purchasing team. We are glad to prepare custom quotes for recurring volumes, private labels and mixed pallets built around your needs. Standard items ship within two business days, while printed or custom sized mailers follow a short production schedule that we confirm in writing before work begins. Every pallet is wrapped, labelled and checked twice, and each shipment carries a packing list that matches your purchase order line by line, so receiving stays simple for your warehouse staff.</p>
    <p>Our account managers visit partners regularly and attend the main trade shows each season. If you would like a sample kit, a price review or a meeting at your site, simply reply to this letter or call our office. We will bring product samples, current stock reports and delivery options so that your team can compare materials side by side and choose the right fit for each order.</p>
    <p>We look forward to working with you and to keeping your shipments safe, tidy and on schedule. Thank you again for considering us as your supplier, and please keep this folder close at hand so the details you need are always ready when your next order comes around.</p>
    <div class="signoff">Yours Sincerely,<strong>Dana Merrow</strong></div>
  </div>
  <div class="signature" role="img" aria-label="Handwritten signature of Dana Merrow"></div>
  <div class="base-rule" style="bottom:0; height:6px;"></div>
  <div class="band" style="left:37px; bottom:0; width:145px; height:6px;">
    <span class="c1"></span><span class="c2"></span><span class="c3"></span>
  </div>
</section>

<!-- Envelope front -->
<section class="piece paper envelope-front" aria-label="Envelope front">
  <div class="wordmark on-light" style="left:18px; top:30px; font-size:17px;">
    <span>Kestrel Wrap</span><span class="wordmark-dot"></span>
  </div>
  <div class="env-address">4200 Harbor Row, Valley Park CA 90000</div>
  <div class="base-rule" style="bottom:0; height:8px;"></div>
  <div class="band" style="left:18px; bottom:0; width:144px; height:8px;">
    <span class="c1"></span><span class="c2"></span><span class="c3"></span>
  </div>
</section>

<!-- Envelope back -->
<section class="piece paper envelope-back" aria-label="Envelope back">
  <svg class="flap" width="466" height="70" viewBox="0 0 466 70" aria-hidden="true">
    <polygon points="0,0 466,0 420,66 46,66" fill="var(--navy)"/>
  </svg>
  <div class="wordmark on-dark centered" style="top:30px; font-size:11px;">
    <span>Kestrel Wrap</span><span class="wordmark-dot"></span>
  </div>
</section>

<!-- Business card front -->
<section class="piece navy card-front" aria-label="Business card front">
  <div class="wordmark on-dark centered" style="top:44px; font-size:12px;">
    <span>Kestrel Wrap</span><span class="wordmark-dot"></span>
  </div>
  <div class="band" style="left:31px; bottom:0; width:109px; height:5px;">
    <span class="c1"></span><span class="c2"></span><span class="c3"></span>
  </div>
</section>

<!-- Business card back -->
<section class="piece paper card-back" aria-label="Business card back">
  <div class="card-name">JORDAN ELLIS</div>
  <div class="card-role">General Manager</div>
  <div class="wordmark on-light" style="left:92px; top:21px; font-size:10px;">
    <span>Kestrel Wrap</span><span class="wordmark-dot"></span>
  </div>
  <div class="card-contact">
    <div class="contact-line"><span class="icon"></span>555-014-2290</div>
    <div class="contact-line"><span class="icon"></span>info@kestrelwrap-example.com</div>
    <div class="contact-line"><span class="icon"></span>www.kestrelwrap-example.com</div>
  </div>
  <div class="card-address">4200 Harbor Row<br>Valley Park CA 90000</div>
  <div class="base-rule" style="bottom:0; height:4px;"></div>
  <div class="band" style="left:86px; bottom:0; width:79px; height:4px;">
    <span class="c1"></span><span class="c2"></span><span class="c3"></span>
  </div>
</section>

</body>
</html>
```